Helpdesk Brochure

Would like to revamp an old brochure for a conference
Can I please add our 1300 857 319 in the footer
Printing this on a double sided Brochure

```html
<!DOCTYPE html>
<html lang="en">
<head>
<meta charset="utf-8">
<title>Northdesk Brochure</title>
<link href="https://fonts.googleapis.com/css2?family=Montserrat:wght@400;500;600;700;800&display=swap" rel="stylesheet">
<style>
:root{
  --orange:#f26a21;
  --dark:#2b2b2e;
  --ink:#333338;
  --muted:#6b6b70;
  --paper:#ffffff;
  --bg:#dedede;
  --photo-desk-a:#d9d4cc;
  --photo-desk-b:#8f8a84;
  --photo-net-a:#0e2233;
  --photo-net-b:#3e7c96;
}
*{box-sizing:border-box;margin:0;padding:0}
html,body{width:723px;height:1200px;overflow:hidden}
body{background:var(--bg);font-family:'Montserrat',sans-serif;color:var(--ink);position:relative}
.spread{position:absolute;top:330px;left:10px;width:703px;display:flex;justify-content:space-between}
.side{width:345px}
.page{width:345px;height:488px;background:var(--paper);position:relative;overflow:hidden;box-shadow:0 3px 10px rgba(0,0,0,.18)}
.side-label{margin-top:18px;text-align:center;font-weight:800;font-size:17px;color:var(--dark);letter-spacing:.5px}

/* front */
.front-top{position:absolute;top:0;right:0;width:200px;height:46px}
.brand{position:absolute;top:14px;left:16px;display:flex;align-items:center;gap:6px;font-weight:800;font-size:15px;color:var(--dark)}
.brand-mark{width:12px;height:12px;background:var(--orange)}
.hero-title{position:absolute;top:56px;left:16px}
.hero-title .kicker{font-weight:700;font-size:11px;color:var(--dark);letter-spacing:.3px}
.hero-title .main{font-weight:800;font-size:27px;color:var(--orange);line-height:1}
.hero-sub{position:absolute;top:98px;left:16px;font-weight:700;font-size:7px;color:var(--dark)}
.hero-text{position:absolute;top:109px;left:16px;width:250px;font-size:5.5px;line-height:1.45;color:var(--muted)}
.photo-desk{position:absolute;top:132px;left:0;width:345px;height:118px;background:linear-gradient(135deg,var(--photo-desk-a),var(--photo-desk-b))}
.photo-accent{position:absolute;top:200px;left:0}
.band{position:absolute;left:0;width:345px;height:24px;background:var(--dark);color:#fff;font-weight:800;font-size:11px;display:flex;align-items:center;justify-content:center;letter-spacing:.3px}
.band.front-band{top:252px}
.services{position:absolute;left:14px;width:317px;display:grid;grid-template-columns:1fr 1fr;column-gap:12px}
.front-services{top:286px;row-gap:14px}
.service{display:flex;gap:6px}
.service-icon{flex:none;width:16px;height:16px;background:var(--orange);display:flex;align-items:center;justify-content:center}
.service h3{font-size:7px;font-weight:800;color:var(--orange);margin-bottom:2px}
.service p{font-size:5.5px;line-height:1.45;color:var(--muted)}

/* footer */
.footer{position:absolute;left:0;bottom:0;width:345px;height:66px}
.contact{position:absolute;left:16px;top:12px;font-size:6px;color:var(--ink);line-height:1.5}
.contact-row{display:flex;align-items:flex-start;gap:5px;margin-bottom:4px}
.cta{position:absolute;right:0;top:6px;width:150px;height:46px;background:var(--orange);color:#fff;padding:6px 0 0 20px;clip-path:polygon(14px 0,100% 0,100% 100%,0 100%)}
.cta .label{font-weight:800;font-size:10px}
.cta .phone{font-weight:800;font-size:17px;display:flex;align-items:center;gap:4px;line-height:1.1}
.footer-strip{position:absolute;left:0;bottom:0;width:345px;height:8px;background:var(--dark)}

/* back */
.back-head{position:absolute;top:0;left:0;width:345px;height:34px;background:var(--dark);color:#fff;font-weight:800;font-size:13px;display:flex;align-items:center;padding-left:70px;letter-spacing:.3px}
.back-head::before{content:"";position:absolute;left:0;top:0;width:56px;height:34px;background:var(--orange);clip-path:polygon(0 0,100% 0,75% 100%,0 100%)}
.back-services{top:50px;row-gap:16px}
.back-services .service.wide{grid-column:1 / span 2;width:50%;margin:0 auto}
.photo-net{position:absolute;top:210px;left:0;width:345px;height:200px;background:radial-gradient(circle at 55% 45%,var(--photo-net-b),var(--photo-net-a) 70%)}
</style>
</head>
<body>
<div class="spread">

  <div class="side">
    <section class="page front">
      <svg class="front-top" viewBox="0 0 200 46" aria-hidden="true">
        <polygon points="40,0 200,0 200,34 28,34" fill="#f26a21"/>
        <polygon points="26,38 200,38 200,44 24,44" fill="#2b2b2e"/>
      </svg>
      <div class="brand"><span class="brand-mark"></span>Northdesk</div>
      <div class="hero-title">
        <div class="kicker">MELBOURNE'S LEADING</div>
        <div class="main">IT SUPPORT</div>
      </div>
      <div class="hero-sub">TAKING CARE OF YOUR IT RESOURCES</div>
      <p class="hero-text">We keep your business connected, secure and productive with responsive local support and proactive technology management.</p>
      <div class="photo-desk" role="img" aria-label="Photo of a laptop on a bright office desk"></div>
      <svg class="photo-accent" width="60" height="52" viewBox="0 0 60 52" aria-hidden="true">
        <polygon points="0,8 40,8 26,22 0,22" fill="#f26a21"/>
        <polygon points="0,28 28,28 18,38 0,38" fill="#2b2b2e"/>
      </svg>
      <div class="band front-band">CLOUD PHONE SYSTEMS &amp; INTERNET</div>
      <div class="services front-services">
        <div class="service">
          <span class="service-icon"><svg width="9" height="9" viewBox="0 0 24 24"><path d="M6 2l4 4-2 3c1 3 4 6 7 7l3-2 4 4-3 4C10 22 2 14 2 5z" fill="#fff"/></svg></span>
          <div><h3>VOIP &amp; PHONE SYSTEMS</h3><p>Cloud phone systems that move with your team, wherever they work.</p></div>
        </div>
        <div class="service">
          <span class="service-icon"><svg width="9" height="9" viewBox="0 0 24 24"><path d="M4 12l5 5L20 6" stroke="#fff" stroke-width="3" fill="none"/></svg></span>
          <div><h3>BROADBAND GATEWAY</h3><p>Fast, reliable internet connections with managed routers and ongoing support.</p></div>
        </div>
        <div class="service">
          <span class="service-icon"><svg width="9" height="9" viewBox="0 0 24 24"><path d="M4 12l5 5L20 6" stroke="#fff" stroke-width="3" fill="none"/></svg></span>
          <div><h3>CLOUD TEAM CALLING</h3><p>Turn your chat app into a full phone system with simple calling.</p></div>
        </div>
        <div class="service">
          <span class="service-icon"><svg width="9" height="9" viewBox="0 0 24 24"><path d="M4 12l5 5L20 6" stroke="#fff" stroke-width="3" fill="none"/></svg></span>
          <div><h3>WIFI, FIBRE &amp; 4G/5G</h3><p>Wireless, fibre and mobile backup links to keep you online.</p></div>
        </div>
      </div>
      <footer class="footer">
        <div class="contact">
          <div class="contact-row"><svg width="8" height="8" viewBox="0 0 24 24"><path d="M12 2a7 7 0 0 0-7 7c0 5 7 13 7 13s7-8 7-13a7 7 0 0 0-7-7zm0 9a2.5 2.5 0 1 1 0-5 2.5 2.5 0 0 1 0 5z" fill="#f26a21"/></svg><span>48 Harbour Street,<br>Carlton VIC 3053</span></div>
          <div class="contact-row"><svg width="8" height="8" viewBox="0 0 24 24"><path d="M2 5h20v14H2z M2 5l10 8 10-8" stroke="#f26a21" stroke-width="2.5" fill="none"/></svg><span>hello@northdeskit.com.au</span></div>
        </div>
        <div class="cta">
          <div class="label">GET IN TOUCH</div>
          <div class="phone"><svg width="12" height="12" viewBox="0 0 24 24"><path d="M6 2l4 4-2 3c1 3 4 6 7 7l3-2 4 4-3 4C10 22 2 14 2 5z" fill="#fff"/></svg>1300 857 319</div>
        </div>
        <div class="footer-strip"></div>
      </footer>
    </section>
    <div class="side-label">FRONT SIDE</div>
  </div>

  <div class="side">
    <section class="page back">
      <div class="back-head">MANAGED I.T SERVICES</div>
      <div class="services back-services">
        <div class="service">
          <span class="service-icon"><svg width="9" height="9" viewBox="0 0 24 24"><path d="M4 12l5 5L20 6" stroke="#fff" stroke-width="3" fill="none"/></svg></span>
          <div><h3>MANAGED I.T SUPPORT</h3><p>Proactive monitoring and helpdesk support that keeps your systems running smoothly.</p></div>
        </div>
        <div class="service">
          <span class="service-icon"><svg width="9" height="9" viewBox="0 0 24 24"><path d="M4 12l5 5L20 6" stroke="#fff" stroke-width="3" fill="none"/></svg></span>
          <div><h3>CYBERSECURITY SOLUTIONS</h3><p>Protect your data with layered security, training and constant threat monitoring.</p></div>
        </div>
        <div class="service">
          <span class="service-icon"><svg width="9" height="9" viewBox="0 0 24 24"><path d="M4 12l5 5L20 6" stroke="#fff" stroke-width="3" fill="none"/></svg></span>
          <div><h3>CLOUD SERVERS &amp; BACKUPS</h3><p>Secure cloud servers and automated backups so nothing important is ever lost.</p></div>
        </div>
        <div class="service">
          <span class="service-icon"><svg width="9" height="9" viewBox="0 0 24 24"><path d="M4 12l5 5L20 6" stroke="#fff" stroke-width="3" fill="none"/></svg></span>
          <div><h3>OFFICE SUITE PACKS</h3><p>Licensing, setup and migration for your full office suite of apps.</p></div>
        </div>
        <div class="service wide">
          <span class="service-icon"><svg width="9" height="9" viewBox="0 0 24 24"><path d="M4 12l5 5L20 6" stroke="#fff" stroke-width="3" fill="none"/></svg></span>
          <div><h3>HARDWARE &amp; WEBSITES</h3><p>Quality hardware supplied and installed, plus websites built and hosted for you.</p></div>
        </div>
      </div>
      <div class="photo-net" role="img" aria-label="Photo of a hand touching a glowing digital network display"></div>
      <footer class="footer">
        <div class="cta" style="left:0;right:auto;clip-path:polygon(0 0,100% 0,calc(100% - 14px) 100%,0 100%);padding-left:16px">
          <div class="label">GET IN TOUCH</div>
          <div class="phone"><svg width="12" height="12" viewBox="0 0 24 24"><path d="M6 2l4 4-2 3c1 3 4 6 7 7l3-2 4 4-3 4C10 22 2 14 2 5z" fill="#fff"/></svg>1300 857 319</div>
        </div>
        <div class="contact" style="left:190px">
          <div class="contact-row"><svg width="8" height="8" viewBox="0 0 24 24"><path d="M12 2a7 7 0 0 0-7 7c0 5 7 13 7 13s7-8 7-13a7 7 0 0 0-7-7zm0 9a2.5 2.5 0 1 1 0-5 2.5 2.5 0 0 1 0 5z" fill="#f26a21"/></svg><span>48 Harbour Street,<br>Carlton VIC 3053</span></div>
          <div class="contact-row"><svg width="8" height="8" viewBox="0 0 24 24"><path d="M2 5h20v14H2z M2 5l10 8 10-8" stroke="#f26a21" stroke-width="2.5" fill="none"/></svg><span>hello@northdeskit.com.au</span></div>
        </div>
        <div class="footer-strip"></div>
      </footer>
    </section>
    <div class="side-label">BACK SIDE</div>
  </div>

</div>
</body>
</html>
```